Business Cards and Stationary for High End Valet Dry Cleaning Service
Brightmere Garment Care "It's fresh pressing in crate!"
Use same font as used in my logo
The font for the business logo should not change. All other details please use your best judgement.
Professional
Dorian Velkoski
Director of Sales and Marketing
41 Parcell Lane
Toronto, Ontario
M5K 3R7
dorian@brightmeregarments.example
www.brightmeregarments.example
IMPORTANT INFORMATION:
Please read the below before starting your design.
Letterheads: I will require 2 sized letterheads with different pieces of information on each.
1st Letterhead:
Normal 8 ½ inches wide by 11 inches long US Letter.
Information to be included: Business Logo, Address, Number, and Web URL
2nd Letterhead:
Legal sized paper 8 ½ inches wide by 14 inches long.
Information to be included: Business Logo, Name, Job Title, Number, Email, and Web URL
IMPORTANT: The goal is to type on this letterhead, print out, fold it a series of times and place it in a 6 ½ inch wide by 3 5/8 inch long envelope. As such, the width of the letterhead must not exceed 6 inches. Please leave the length at 14 inches. Please center the letterhead accordingly and only allow for 6 inches in width.
Envelopes: I will require 2 sized envelopes with different pieces of information on each.
1st Envelope:
Standard envelope for a 8 ½ inch wide by 11 inch long letter sized document.
2nd Envelope:
6 ½ inch wide by 3 5/8 inch long. The front should be the business logo, the back use your discretion.
Order Form: I will require a revision of the existing order form. A PDF file has been attached. Please replace existing logo with the current logo. As per the footer, please keep existing phone number and Web URL but replace ‘orders@brightmeregarments.example’ with ‘dorian@brightmeregarments.example’. Also, where it reads ‘Company Name’ it should read ‘Company/Building Name’.
IMPORTANT: Each order form will be printed and folded and will be placed in a plastic casing measuring 4 inches wide by 2.5 inches in length. Please make the necessary adjustments without sacrificing any of the detail.
Email Signature: I would like an email signature with the following details: Logo, Name, Job Title, Number, Email, and Web URL.
Would like the entire logo to take the space. This includes the logo, tag line and the perforated lines.
This is the company logo.
This is the existing Order Form that needs revising. Please replace existing logo with new logo or some form of it. Please make amendment to the footer as follows: please keep the phone number, and web URL but replace 'orders@brightmeregarments.example' with 'dorian@brightmeregarments.example'. Please note: each order form should be 4 inches in width by 2.5 inches in length. These will be incased in a plastic accordingly.

```html
<!DOCTYPE html>
<html lang="en">
<head>
<meta charset="utf-8">
<title>Brightmere Garment Care — Stationery Suite</title>
<link href="https://fonts.googleapis.com/css2?family=Cormorant+Garamond:wght@600&family=Lato:wght@400;700&display=swap" rel="stylesheet">
<style>
  :root{
    --ground:#2b2a29;
    --paper:#ffffff;
    --navy:#1c237a;
    --royal:#3b4fd0;
    --gold:#eaa445;
    --gold-light:#f6d49a;
    --ink:#2c2f4a;
    --rule:#c9cde3;
  }
  *{box-sizing:border-box;margin:0;padding:0}
  html,body{width:1200px;height:394px;overflow:hidden;background:var(--ground)}
  body{position:relative;font-family:"Lato",sans-serif;color:var(--ink)}
  .piece{position:absolute;background:var(--paper);overflow:hidden;box-shadow:0 2px 6px rgba(0,0,0,.45)}
  .band-blue{background:linear-gradient(100deg,var(--navy) 0%,var(--royal) 60%,var(--navy) 100%)}
  .band-gold{position:absolute;left:0;right:0;bottom:0;height:6px;background:linear-gradient(90deg,var(--gold-light),var(--gold) 40%,var(--gold))}
  .band-gold::before{content:"";position:absolute;left:0;right:0;top:-2px;height:2px;background:var(--royal)}
  .brand{display:flex;align-items:center;gap:3px;color:var(--paper);font-family:"Cormorant Garamond",serif;font-weight:600;line-height:1;white-space:nowrap}
  .brand-dot{border-radius:50%;border:1px solid var(--gold);flex:none}
  .contact{color:var(--paper);font-size:3.4px;line-height:1.35;text-align:right}

  /* business cards */
  .card{left:17px;width:74px;height:32px;border-radius:1px}
  .card-front{top:161px;display:flex;align-items:center;justify-content:center}
  .card-front .brand{font-size:6px}
  .card-front .brand-dot{width:8px;height:8px}
  .card-back{top:197px;padding:4px}
  .card-back .name{color:var(--paper);font-size:4.4px;font-weight:700}
  .card-back .title{color:var(--gold);font-size:3px;margin-bottom:3px}
  .card-back .contact{text-align:left;font-size:3px}

  /* letter letterhead */
  .letter{left:144px;top:34px;width:168px;height:326px}
  .letter .header{height:28px;display:flex;align-items:center;justify-content:space-between;padding:0 8px}
  .letter .brand{font-size:6px}
  .letter .brand-dot{width:9px;height:9px}

  /* legal letterhead */
  .legal{left:350px;top:24px;width:200px;height:360px}
  .legal .header{height:26px;display:flex;align-items:center;justify-content:space-between;padding:0 28px}
  .legal .brand{font-size:6px}
  .legal .brand-dot{width:9px;height:9px}

  /* large envelope */
  .envelope{left:576px;top:34px;width:192px;height:333px}
  .envelope svg{position:absolute;left:0;top:0}
  .envelope .brand{position:absolute;left:50%;top:34px;transform:translateX(-50%);font-size:6px}
  .envelope .brand-dot{width:9px;height:9px}

  /* small envelopes */
  .small{left:799px;width:101px}
  .small-back{top:113px;height:62px}
  .small-back svg{position:absolute;left:0;top:0}
  .small-front{top:190px;height:52px}
  .small-front .corner{position:absolute;left:4px;top:4px}
  .small-front .brand{color:var(--navy);font-size:4.4px}
  .small-front .brand-dot{width:6px;height:6px;border-color:var(--navy)}

  /* order form */
  .order{left:1032px;top:96px;width:96px;height:144px;padding:0}
  .order .header{height:18px;display:flex;align-items:center;justify-content:center}
  .order .brand{font-size:5px}
  .order .brand-dot{width:7px;height:7px}
  .order .body{padding:4px 6px;font-size:3.4px}
  .order h2{font-size:5px;color:var(--navy);margin-bottom:3px}
  .order .field{display:flex;gap:2px;margin-bottom:3px}
  .order .field span:last-child{flex:1;border-bottom:.5px solid var(--rule)}
  .order table{width:100%;border-collapse:collapse;margin-top:4px}
  .order td{border:.5px solid var(--rule);height:6px}
  .order td.check{width:7px;background:#e9ecf8}
  .order .footer{position:absolute;left:0;right:0;bottom:0;height:10px;font-size:3px;color:var(--paper);display:flex;align-items:center;justify-content:center}

  /* email signature */
  .signature{left:1032px;top:252px;width:161px;height:43px;display:flex;align-items:stretch}
  .signature .logo-panel{width:64px;display:flex;align-items:center;justify-content:center}
  .signature .brand{font-size:5px}
  .signature .brand-dot{width:7px;height:7px}
  .signature .details{padding:5px 6px;font-size:3.6px;line-height:1.4}
  .signature .name{font-size:5px;font-weight:700;color:var(--navy)}
  .signature .title{color:var(--gold);margin-bottom:2px}
</style>
</head>
<body>

  <section class="piece band-blue card card-front">
    <div class="brand"><span class="brand-dot"></span>Brightmere Garment Care</div>
  </section>
  <section class="piece band-blue card card-back">
    <p class="name">Dorian Velkoski</p>
    <p class="title">Director of Sales and Marketing</p>
    <p class="contact">41 Parcell Lane, Toronto, Ontario M5K 3R7<br>T 416-555-0192<br>dorian@brightmeregarments.example<br>www.brightmeregarments.example</p>
  </section>

  <section class="piece letter">
    <header class="header band-blue">
      <div class="brand"><span class="brand-dot"></span>Brightmere Garment Care</div>
      <p class="contact">41 Parcell Lane<br>Toronto, Ontario M5K 3R7<br>T 416-555-0192<br>www.brightmeregarments.example</p>
    </header>
    <div class="band-gold"></div>
  </section>

  <section class="piece legal">
    <header class="header band-blue">
      <div class="brand"><span class="brand-dot"></span>Brightmere Garment Care</div>
      <p class="contact">Dorian Velkoski<br>Director of Sales and Marketing<br>T 416-555-0192<br>dorian@brightmeregarments.example</p>
    </header>
    <div class="band-gold"></div>
  </section>

  <section class="piece envelope">
    <svg width="192" height="70" viewBox="0 0 192 70" aria-hidden="true">
      <defs><linearGradient id="flapBlue" x1="0" x2="1"><stop offset="0" stop-color="#1c237a"/><stop offset=".6" stop-color="#3b4fd0"/><stop offset="1" stop-color="#1c237a"/></linearGradient></defs>
      <path d="M0 0H192V18L96 66L0 18Z" fill="url(#flapBlue)"/>
    </svg>
    <div class="brand"><span class="brand-dot"></span>Brightmere Garment Care</div>
    <div class="band-gold"></div>
  </section>

  <section class="piece small small-back">
    <svg width="101" height="40" viewBox="0 0 101 40" aria-hidden="true">
      <defs><linearGradient id="smallFlap" x1="0" x2="1"><stop offset="0" stop-color="#1c237a"/><stop offset=".6" stop-color="#3b4fd0"/><stop offset="1" stop-color="#1c237a"/></linearGradient></defs>
      <path d="M0 0H101V6L50.5 36L0 6Z" fill="url(#smallFlap)"/>
    </svg>
  </section>
  <section class="piece small small-front">
    <div class="corner"><div class="brand"><span class="brand-dot"></span>Brightmere Garment Care</div></div>
    <div class="band-gold"></div>
  </section>

  <section class="piece order">
    <header class="header band-blue">
      <div class="brand"><span class="brand-dot"></span>Brightmere Garment Care</div>
    </header>
    <div class="body">
      <h2>Order Form</h2>
      <div class="field"><span>Name</span><span></span></div>
      <div class="field"><span>Company/Building Name</span><span></span></div>
      <div class="field"><span>Suite</span><span></span></div>
      <div class="field"><span>Phone</span><span></span></div>
      <table>
        <tr><td class="check"></td><td>Shirts laundered</td></tr>
        <tr><td class="check"></td><td>Dry clean</td></tr>
        <tr><td class="check"></td><td>Press only</td></tr>
        <tr><td class="check"></td><td>Repairs</td></tr>
      </table>
    </div>
    <footer class="footer band-blue">416-555-0192 · dorian@brightmeregarments.example</footer>
  </section>

  <section class="piece signature">
    <div class="logo-panel band-blue">
      <div class="brand"><span class="brand-dot"></span>Brightmere Garment Care</div>
    </div>
    <div class="details">
      <p class="name">Dorian Velkoski</p>
      <p class="title">Director of Sales and Marketing</p>
      <p>T 416-555-0192</p>
      <p>dorian@brightmeregarments.example</p>
      <p>www.brightmeregarments.example</p>
    </div>
  </section>

</body>
</html>
```